bluecastle aquatics business card

I need a new attractive business card. I am planning on printing on very thick rounded corner stock and having painted edges. We are a swimming pool remodel, repair, and service company in north florida. Our current logo is red, white, and blue. It doesn't necessarily have to stay that way, I am open to other ideas. It will need to contain my name, work and cell numbers, email, website, and my contractor license number.

Target Market(s)

High end residential and commercial clients

Industry/Entity Type

Business

Contact Information for Business Card

Company name, employee name and title, work and cell phone numbers, email and website, and Contractor number.

our work scope should be on card somewhere: remodel ~ repair ~ service

logo or slight variation of logo also. (not necessarily set on keeping exact logo)

Colors

Designer to choose colors to be used in the design.

Requirements
Nice to have
• We deal with water so I think some sort of water element or just a color similar to pool water would be nice to integrate into design.

```html
<!DOCTYPE html>
<html lang="en">
<head>
<meta charset="utf-8">
<title>Bluecastle Aquatics – Business Card</title>
<link rel="stylesheet" href="https://fonts.googleapis.com/css2?family=Cinzel:wght@600;700&family=Lato:wght@400;700&display=swap">
<style>
  :root {
    --pool-blue: #1f7cc8;
    --deep-blue: #1565b0;
    --water-light: #5bc2ee;
    --water-mid: #2a9ad9;
    --water-deep: #1679bf;
    --signal-red: #e3232c;
    --paper: #f7f8f9;
    --paper-shade: #e9ecee;
    --backdrop: #d9dcdf;
    --white: #ffffff;
  }
  * { box-sizing: border-box; margin: 0; padding: 0; }
  html, body { width: 1200px; height: 913px; overflow: hidden; }
  body {
    background: var(--backdrop);
    font-family: "Lato", sans-serif;
    position: relative;
  }
  .card {
    position: absolute;
    top: 300px;
    width: 540px;
    height: 310px;
    border-radius: 18px;
    border: 2px solid var(--signal-red);
    overflow: hidden;
    box-shadow: 0 6px 18px rgba(0,0,0,.18);
  }
  /* Front */
  .card-front {
    left: 50px;
    background: radial-gradient(ellipse at 30% 40%, var(--white), var(--paper) 55%, var(--paper-shade));
  }
  .accent-block {
    position: absolute; left: 0; top: 62px;
    width: 44px; height: 26px; background: var(--signal-red);
  }
  .holder-name {
    position: absolute; left: 56px; top: 60px;
    font-family: "Cinzel", serif; font-weight: 700;
    font-size: 22px; color: var(--signal-red); letter-spacing: .5px;
  }
  .holder-title {
    position: absolute; left: 56px; top: 90px;
    font-size: 13px; color: var(--pool-blue);
  }
  .divider {
    position: absolute; left: 56px; top: 110px;
    width: 220px; height: 1px; background: var(--pool-blue);
  }
  .contact-list {
    position: absolute; left: 36px; top: 124px;
    list-style: none; font-size: 13px; color: var(--pool-blue); line-height: 21px;
  }
  .contact-list li { display: flex; align-items: center; gap: 8px; }
  .contact-list svg { width: 12px; height: 12px; flex: none; }
  .brand-name {
    font-family: "Cinzel", serif; font-weight: 700;
    color: var(--pool-blue); letter-spacing: 1.5px; white-space: nowrap;
  }
  .card-front .brand-name {
    position: absolute; right: 30px; top: 150px; font-size: 20px;
  }
  .license {
    position: absolute; left: 250px; top: 240px;
    font-size: 14px; font-weight: 700;
  }
  .license-label { color: var(--signal-red); }
  .license-number { color: var(--pool-blue); }
  .base-bar {
    position: absolute; left: 180px; bottom: 0;
    width: 180px; height: 12px; background: var(--deep-blue);
  }
  /* Back */
  .card-back { left: 610px; }
  .water-surface {
    position: absolute; inset: 0;
    background: radial-gradient(ellipse at 40% 35%, var(--water-light), var(--water-mid) 55%, var(--water-deep));
  }
  .back-content {
    position: absolute; inset: 0;
    display: flex; flex-direction: column; align-items: center; justify-content: center; gap: 22px;
  }
  .card-back .brand-name { color: var(--white); font-size: 28px; }
  .scope {
    font-family: "Cinzel", serif; font-weight: 600;
    font-size: 18px; color: var(--white); letter-spacing: 2px;
  }
</style>
</head>
<body>

<section class="card card-front">
  <div class="accent-block"></div>
  <h1 class="holder-name">Daniel R. Moore</h1>
  <p class="holder-title">CEO/Founder</p>
  <div class="divider"></div>
  <ul class="contact-list">
    <li><svg viewBox="0 0 12 12"><path d="M2 1l2 0 1 3-1.5 1a6 6 0 0 0 3 3L7.5 6.5l3 1v2l-1 1.5C5 11 1 7 1 2z" fill="var(--signal-red)"/></svg>(904) 555-0142</li>
    <li><svg viewBox="0 0 12 12"><rect x="3" y="0.5" width="6" height="11" rx="1" fill="none" stroke="var(--signal-red)" stroke-width="1.2"/></svg>(904) 555-0187</li>
    <li><svg viewBox="0 0 12 12"><rect x="0.5" y="2" width="11" height="8" fill="var(--signal-red)"/><path d="M1 2.5l5 4 5-4" fill="none" stroke="var(--white)" stroke-width="1"/></svg>moore@bluecastleaquatics.com</li>
    <li><svg viewBox="0 0 12 12"><circle cx="6" cy="6" r="5.5" fill="var(--signal-red)"/><path d="M0.5 6h11M6 .5v11" stroke="var(--white)" stroke-width=".8"/></svg>www.bluecastleaquatics.com</li>
  </ul>
  <p class="brand-name">Bluecastle Aquatics</p>
  <p class="license"><span class="license-label">Contractor No:</span> <span class="license-number">0458-2139</span></p>
  <div class="base-bar"></div>
</section>

<section class="card card-back">
  <div class="water-surface" role="img" aria-label="Photograph of rippling blue pool water"></div>
  <div class="back-content">
    <p class="brand-name">Bluecastle Aquatics</p>
    <p class="scope">Remodel • Repair • Service</p>
  </div>
</section>

</body>
</html>
```